We need a company profile design 8 + cover

The company profile is attached below, we need to renew the whole thing with full modification. content and page arrangement is the same. All should be A5 size printable and electronic copies.

I attached logo and colors for identity, please use logo colors as main scheme colours

We need 2 copies Arabic and English

Font styles to use
Sans Serif

Requirements
Nice to have
• Please let us know how we can use the designs to edit in Arabic

```html
<!DOCTYPE html>
<html lang="en">
<head>
<meta charset="utf-8">
<title>Nova Scholar – Company Profile</title>
<link href="https://fonts.googleapis.com/css2?family=Montserrat:wght@400;500;600;700;800&family=Roboto+Condensed:wght@300;400;700&display=swap" rel="stylesheet">
<style>
:root{
  --navy:#22398c;
  --navy-dark:#17286b;
  --navy-light:#3450b0;
  --green:#8cc63f;
  --green-dark:#76ad2e;
  --ink:#222;
  --body:#444;
  --stage:#e6e6e6;
  --label:#444;
}
*{margin:0;padding:0;box-sizing:border-box}
html,body{width:1200px;height:1184px;overflow:hidden}
body{background:var(--stage);font-family:"Montserrat",sans-serif;position:relative;color:var(--body)}
.page{position:absolute;width:352px;height:499px;background:#fff;overflow:hidden;box-shadow:0 16px 14px -10px rgba(0,0,0,.4)}
.page-label{position:absolute;width:352px;text-align:center;font-size:24px;color:var(--label);font-weight:400;letter-spacing:.5px}
.abs{position:absolute}
.condensed{font-family:"Roboto Condensed",sans-serif}
.p-text{font-size:6px;line-height:1.5;color:var(--body)}
.wrap-cut{float:left;width:96px;height:22px;shape-outside:polygon(0 0,100% 0,0 100%)}
.section-title{font-family:"Roboto Condensed",sans-serif;font-weight:400;color:var(--green);font-size:17px;border-bottom:1px solid var(--green);padding-bottom:1px;white-space:nowrap}
.footer-band{position:absolute;left:0;width:352px;height:18px;background:var(--navy);color:#fff;font-size:5px;display:flex;align-items:center;padding:0 12px;gap:6px}
.footer-band .num{margin-left:auto}
.footer-rule{position:absolute;left:0;width:352px;height:1.5px;background:var(--navy)}
.brand-name{font-family:"Montserrat",sans-serif;font-weight:800;color:var(--navy);text-align:center;line-height:1}
.contact-top{position:absolute;left:12px;top:28px;color:#fff;font-family:"Roboto Condensed",sans-serif;font-size:9px;line-height:1.25}
.service{position:absolute;left:12px;right:12px}
.service .icon{position:absolute;left:0;top:0;width:20px;height:20px;border-radius:50%;background:var(--green);border:2px solid #cfe6ae}
.service .icon::after{content:"";position:absolute;left:5px;top:5px;width:6px;height:6px;border:1.5px solid #fff;border-radius:2px}
.service h4{margin-left:26px;font-size:7px;font-weight:700;color:var(--navy);display:inline-block;border-bottom:1px solid var(--navy);padding-bottom:1px;font-family:"Roboto Condensed",sans-serif}
.service p{margin-left:26px;font-size:5.8px;line-height:1.5;color:var(--body);margin-top:3px;text-align:justify}
.quote-mark{position:absolute;font-family:"Montserrat",sans-serif;font-weight:800;color:var(--green);font-size:30px;line-height:1}
.quote-box{position:absolute;top:179px;height:40px;background:var(--navy);color:#fff;font-size:6.2px;text-align:center;padding-top:8px;line-height:1.4}
.quote-box small{display:block;font-size:3.6px;opacity:.85;margin-top:2px}
.photo{position:absolute;background:linear-gradient(160deg,#c9c6bf,#8c8275)}
.back-info{position:absolute;left:0;width:352px;text-align:center;color:#fff}
.back-info h5{font-size:7.5px;font-weight:700;text-decoration:underline;margin-bottom:5px}
.back-info p{font-size:7px;line-height:1.6}
.social{display:flex;justify-content:center;gap:8px}
.social span{width:10px;height:10px;border:1px solid #fff;border-radius:50%}
.cover-headline{position:absolute;left:12px;top:246px;line-height:1.05}
.cover-headline .line-green{color:var(--green);font-family:"Roboto Condensed",sans-serif;font-weight:700}
.cover-headline .line-white{color:#fff}
</style>
</head>
<body>

<!-- COVER -->
<section class="page cover" style="left:29px;top:29px">
  <div class="photo" role="img" aria-label="Group photo of smiling students sitting together on a staircase" style="left:98px;top:0;width:254px;height:299px;clip-path:polygon(0 0,100% 0,100% 100%,30% 100%,0 63%);background:linear-gradient(160deg,#7a6a5c,#3b332d 55%,#6b5344)"></div>
  <svg class="abs" style="left:0;top:0" width="352" height="499" viewBox="0 0 352 499">
    <polygon points="0,147 68,147 175,295 72,452 0,452" fill="#22398c"/>
    <polygon points="68,147 78,147 185,295 175,295" fill="#3450b0"/>
    <polygon points="175,295 185,295 82,452 72,452" fill="#3450b0"/>
    <line x1="112" y1="372" x2="78" y2="432" stroke="#fff" stroke-width=".8"/>
    <line x1="104" y1="372" x2="70" y2="432" stroke="#fff" stroke-width=".8"/>
    <rect x="0" y="452" width="352" height="28" fill="#22398c"/>
    <rect x="0" y="484" width="352" height="2" fill="#22398c"/>
    <line x1="0" y1="466" x2="352" y2="466" stroke="#fff" stroke-width=".6" stroke-dasharray="3 2"/>
    <line x1="0" y1="139" x2="45" y2="139" stroke="#8cc63f" stroke-width="1"/>
  </svg>
  <div class="brand-name abs" style="left:10px;top:60px;width:110px;font-size:22px">NOVA<br><span style="font-size:13px">SCHOLAR</span></div>
  <div class="cover-headline">
    <div class="line-green" style="font-size:18px">YOUR ACADEMIC</div>
    <div class="line-white" style="font-size:19px;font-weight:600">DREAMS IS</div>
    <div class="line-green" style="font-size:15px">OUR IMPORTANT</div>
    <div class="line-white condensed" style="font-size:42px;font-weight:400;line-height:1">CHOICE</div>
  </div>
  <div class="abs" style="right:12px;top:338px;text-align:right;line-height:1.05">
    <div style="color:var(--green);font-weight:800;font-size:19px">ACADEMIC AND</div>
    <div class="condensed" style="color:var(--ink);font-weight:300;font-size:27px">STUDY ABROAD</div>
    <div style="color:var(--green);font-weight:800;font-size:37px">SERVICES</div>
  </div>
  <div class="abs" style="left:118px;top:459px;text-align:center;color:#fff;font-size:8.5px;letter-spacing:3.5px;background:var(--navy);padding:0 6px">www.novascholar.example</div>
</section>
<div class="page-label" style="left:29px;top:549px">Cover Page</div>

<!-- PAGE 01 -->
<section class="page who-we-are" style="left:423px;top:29px">
  <svg class="abs" style="left:0;top:0" width="352" height="100" viewBox="0 0 352 100">
    <polygon points="0,0 280,0 0,73" fill="#22398c"/>
    <polygon points="280,0 290,0 0,78 0,73" fill="#3450b0"/>
  </svg>
  <svg class="abs" style="left:36px;top:14px" width="12" height="10" viewBox="0 0 12 10"><path d="M1 4 Q6 0 11 4 L9 5 L8 3.5 L4 3.5 L3 5Z M3 5 L9 5 L10 9 L2 9Z" fill="#fff"/></svg>
  <div class="contact-top" style="top:35px">+971 55 210 4480<br>+971 56 372 9016</div>
  <div class="section-title abs" style="right:12px;top:34px">WHO WE ARE</div>
  <div class="abs p-text" style="left:12px;right:24px;top:64px;text-align:right">
    <span class="wrap-cut"></span>
    services in UAE. It is officially recognized by National Education Council, Global Learning Board, International Agent Network and QS-100 quality standard. Established in 2015, NOVA SCHOLAR provides professional consultancy services to help aspiring students find a suitable overseas educational institution in USA, UK, Australia, Malaysia, Europe, Middle East, South Africa and more. We take pride in our holistic program that helps every student make the right career choice, find the right course, what the student need and the government vision. We act as study abroad consultants for various government sectors and corporations.
  </div>
  <div class="abs" style="left:334px;top:62px;width:3px;height:74px;background:var(--navy)"></div>
  <div class="quote-mark" style="left:86px;top:164px">“</div>
  <div class="quote-mark" style="left:246px;top:164px">“</div>
  <div class="quote-box" style="left:12px;width:161px">There is no place in the future for those who<br>lack science and knowledge<small>— Karim Al Mansoori —</small></div>
  <div class="quote-box" style="left:181px;width:160px">Education is the most powerful weapon<br>which you can use to change the world<small>— Karim Al Mansoori —</small></div>
  <div class="photo" role="img" aria-label="Portrait photo of the first quoted leader" style="left:20px;top:219px;width:153px;height:100px;background:linear-gradient(160deg,#eef0f2,#d8d4cc 50%,#b69c82)"></div>
  <div class="photo" role="img" aria-label="Portrait photo of the second quoted leader" style="left:181px;top:219px;width:153px;height:100px;background:linear-gradient(160deg,#4a4034,#2a2622 55%,#c9a52a)"></div>
  <div class="section-title abs" style="left:12px;top:355px">VISION &amp; MISSION</div>
  <div class="abs" style="left:14px;top:382px;width:3px;height:72px;background:var(--navy)"></div>
  <div class="abs p-text" style="left:28px;right:12px;top:382px">
    <p>To be leading the educational consultancy in the region by providing customized and up to date educational services to students and educational institutions abroad.</p>
    <p style="margin-top:8px">To provide students from all the countries with the needed and qualified services for abroad studies through an integrated system of facilities, consultancy services and guidance through building strategic partnerships with the best universities from all over the world.</p>
  </div>
  <div class="footer-band" style="top:471px"><span>◉ www.novascholar.example</span><span>|</span><span>✉ hello@novascholar.example</span><span>|</span><span>⚲ UAE | Abu Dhabi</span><span class="num">01</span></div>
  <div class="footer-rule" style="top:492px"></div>
</section>
<div class="page-label" style="left:423px;top:549px">Page - 01</div>

<!-- PAGE 02 -->
<section class="page values" style="left:816px;top:29px">
  <div class="abs" style="left:0;top:0;width:352px;height:11px;background:var(--navy)"></div>
  <div class="section-title abs" style="left:131px;top:28px">OUR VALUES</div>
  <svg class="abs" style="left:0;top:0" width="352" height="180" viewBox="0 0 352 180" font-family="Montserrat,sans-serif" font-size="5.5" font-weight="700" text-anchor="middle">
    <g fill="#22398c" stroke="#22398c">
      <path d="M12 114 H72 A30 20 0 0 1 12 114Z" stroke="none"/>
      <line x1="42" y1="134" x2="42" y2="150" stroke-width="1.5"/>
      <circle cx="42" cy="157" r="7" fill="#fff" stroke-width="2"/><circle cx="42" cy="157" r="3" stroke="none"/>
      <path d="M146 114 H206 A30 20 0 0 1 146 114Z" stroke="none"/>
      <line x1="176" y1="134" x2="176" y2="150" stroke-width="1.5"/>
      <circle cx="176" cy="157" r="7" fill="#fff" stroke-width="2"/><circle cx="176" cy="157" r="3" stroke="none"/>
      <path d="M280 114 H340 A30 20 0 0 1 280 114Z" stroke="none"/>
      <line x1="310" y1="134" x2="310" y2="150" stroke-width="1.5"/>
      <circle cx="310" cy="157" r="7" fill="#fff" stroke-width="2"/><circle cx="310" cy="157" r="3" stroke="none"/>
    </g>
    <g fill="#8cc63f" stroke="#8cc63f">
      <path d="M79 114 H141 A31 22 0 0 0 79 114Z" stroke="none"/>
      <line x1="110" y1="92" x2="110" y2="77" stroke-width="1.5"/>
      <circle cx="110" cy="70" r="7" fill="#fff" stroke-width="2"/><circle cx="110" cy="70" r="3" stroke="none"/>
      <path d="M212 114 H274 A31 22 0 0 0 212 114Z" stroke="none"/>
      <line x1="243" y1="92" x2="243" y2="77" stroke-width="1.5"/>
      <circle cx="243" cy="70" r="7" fill="#fff" stroke-width="2"/><circle cx="243" cy="70" r="3" stroke="none"/>
    </g>
    <g fill="#22398c">
      <text x="42" y="107">Credibility</text>
      <text x="176" y="100">Excellence in</text><text x="176" y="107">Services delivery</text>
      <text x="310" y="83">Implementing best</text><text x="310" y="91">practises in the</text><text x="310" y="99">educational</text><text x="310" y="107">consultancy</text>
    </g>
    <g fill="#8cc63f">
      <text x="110" y="124">Social</text><text x="110" y="131">Responsibility</text>
      <text x="243" y="124">Strengthening</text><text x="243" y="131">Partnerships</text>
    </g>
  </svg>
  <div class="abs" style="left:0;top:183px;width:352px;height:77px;background:var(--navy)"></div>
  <div class="abs condensed" style="left:12px;top:195px;color:#fff;font-size:33px;font-weight:400;line-height:.95">WHAT<br>WE DO</div>
  <div class="abs" style="left:112px;top:190px;width:1px;height:63px;background:#fff;opacity:.8"></div>
  <div class="abs" style="left:120px;right:12px;top:193px;color:#fff;font-size:6.2px;line-height:1.6;text-align:justify">NOVA SCHOLAR offers professional consultation to local and international students on a wide variety of educational programs covering summer and English programs, pathway courses, undergraduate, postgraduate degree programs and PHD courses. We specialize in providing professional assistance to students of various age groups. We help students through each stage.</div>
  <div class="service" style="top:276px"><span class="icon"></span><h4>FREE ACADEMIC CONSULTING</h4><p>We get to understand the student's academic, social, and personal backgrounds and then provide them with various career options.</p></div>
  <div class="service" style="top:320px"><span class="icon"></span><h4>COURSE SELECTION</h4><p>We assist our students in finding them right and correct courses based on their interests. Courses that are suitable to the industry in uplifting their professional levels for a successful career.</p></div>
  <div class="service" style="top:372px"><span class="icon"></span><h4>APPLICATION SUBMISSION</h4><p>We help save the students' time and energy by providing advice through the entire process of application. Providing assistance with the required documents, deadlines, and personal statement editing etc.</p></div>
  <div class="service" style="top:422px"><span class="icon"></span><h4>UNIVERSITY SELECTION</h4><p style="margin-right:110px;text-align:left">Selecting a university involves a holistic consideration of all aspects of an educational institution including facilities and future prospects. We look at each and every detail as we guide our students.</p></div>
  <svg class="abs" style="left:0;top:440px" width="352" height="59" viewBox="0 0 352 59">
    <polygon points="205,59 352,18 352,59" fill="#22398c"/>
    <polygon points="192,59 352,14 352,18 205,59" fill="#3450b0"/>
    <text x="338" y="52" fill="#fff" font-size="6" font-family="Montserrat,sans-serif" text-anchor="end">02</text>
  </svg>
</section>
<div class="page-label" style="left:816px;top:549px">Page - 02</div>

<!-- PAGE 03 -->
<section class="page services" style="left:29px;top:606px">
  <svg class="abs" style="left:0;top:0" width="352" height="100" viewBox="0 0 352 100">
    <polygon points="0,0 280,0 0,73" fill="#22398c"/>
    <polygon points="280,0 290,0 0,78 0,73" fill="#3450b0"/>
  </svg>
  <svg class="abs" style="left:36px;top:14px" width="12" height="10" viewBox="0 0 12 10"><path d="M1 4 Q6 0 11 4 L9 5 L8 3.5 L4 3.5 L3 5Z M3 5 L9 5 L10 9 L2 9Z" fill="#fff"/></svg>
  <div class="contact-top" style="top:29px">+971 55 210 4480<br>+971 56 372 9016</div>
  <div class="abs" style="right:12px;top:36px;text-align:right;line-height:1">
    <div style="color:var(--green);font-weight:800;font-size:21px">WE ARE READY</div>
    <div class="condensed" style="color:var(--ink);font-weight:300;font-size:34px;margin-top:2px">TO SERVE YOU 24 X 7</div>
  </div>
  <div class="service" style="top:111px"><span class="icon"></span><h4>QUICK ADMISSION DECISIONS</h4><p>NOVA SCHOLAR makes it easy for students by proactively contacting the universities for getting timely offers. In addition, we help resolve all minor issues in the offers.</p></div>
  <div class="service" style="top:162px"><span class="icon"></span><h4>SCHOLARSHIP ADVICE</h4><p>We help our students in advising them to various scholarships offered by universities and government sectors and assist them with the entire application process.</p></div>
  <div class="service" style="top:213px"><span class="icon"></span><h4>ACCOMMODATION</h4><p>We assist our students by providing information on various available accommodations like on campus, off campus, Homestays, Student housing, Residential accommodation so on and so forth.</p></div>
  <div class="service" style="top:272px"><span class="icon"></span><h4>VISA ASSISTANCE</h4><p>Applying for visa is a critical part of overseas education preparation. Our professional consultants provide our students with a checklist for visa processing, and help them prepare for visa interviews.</p></div>
  <div class="service" style="top:331px"><span class="icon"></span><h4>OTHER SERVICES</h4><p>Our other services include, providing assistance in organizing Insurance, airport pick-ups, pre-departure advice etc and many more information to make the journey hassle free and comfortable.</p></div>
  <div class="service" style="top:391px"><span class="icon"></span><h4>LANGUAGES AND PREPARATION PROGRAMS</h4><p>Our tie up connections with colleges and language schools offering courses that help in meeting essential requirements at various universities helping them secure admissions for degree programs.</p></div>
  <div class="footer-band" style="top:471px"><span>◉ www.novascholar.example</span><span>|</span><span>✉ hello@novascholar.example</span><span>|</span><span>⚲ UAE | Abu Dhabi</span><span class="num">03</span></div>
  <div class="footer-rule" style="top:492px"></div>
</section>
<div class="page-label" style="left:29px;top:1127px">Page - 03</div>

<!-- BACK PAGE -->
<section class="page back" style="left:423px;top:606px">
  <div class="photo" role="img" aria-label="Photo of a smiling student talking with an advisor in a bright office" style="left:0;top:0;width:352px;height:482px;background:linear-gradient(180deg,#dfeeee 0%,#cfe3e6 40%,#8fa8b2 75%,#2a3a4e 100%)"></div>
  <div class="brand-name abs" style="left:0;top:74px;width:352px;font-size:44px">NOVA<br><span style="font-size:20px">SCHOLAR</span></div>
  <div class="abs" style="left:0;top:314px;width:352px;height:136px;background:rgba(140,198,63,.93)"></div>
  <div class="back-info" style="top:322px"><h5>ADDRESS</h5><p>Palm Crescent Arena<br>Harbor Sports Club, Suite 31, 3rd Floor, PO Box – 7720</p></div>
  <div class="back-info" style="top:367px"><h5>CONTACT US</h5><p>+971 2 418 30 30 &nbsp;/&nbsp; +971 55 210 4480 &nbsp;/&nbsp; +971 507731264 &nbsp;/&nbsp; +971 56 372 9016</p></div>
  <div class="back-info" style="top:408px"><h5>FOLLOW US</h5><div class="social"><span></span><span></span><span></span><span></span><span></span></div></div>
  <div class="abs" style="left:0;top:450px;width:352px;height:32px;background:var(--navy-dark)"></div>
  <div class="footer-rule" style="top:486px"></div>
</section>
<div class="page-label" style="left:423px;top:1127px">Back Page</div>

<!-- Standalone brand name -->
<div class="brand-name abs" style="left:880px;top:850px;width:220px;color:#262626;font-size:58px">NOVA<br><span style="font-size:28px">SCHOLAR</span></div>

</body>
</html>
```